Support People to improve their image and well-being by provided personalised advise

We need a design for business cards that could be used for production on plato press. We build a new business in our region for advising mostly women (also men though) on style embracing several aspects including fashion, style, self-confidence and ultimately your internal and external image. The business card should be "classy", "french-style". The business is located in the french -speaking part of Switzerland, close to France. The name of the company is Velo Grace

Target Market(s)

Service fees won't be cheap (medium to premium) thus we target mid-class to upper-class women (1st target) and men (2nd target)

Industry/Entity Type

Life Coaching

Contact Information for Business Card

Conseil en Image

+41 79 418 62 07
morinetu@velo-grace.ch
linkedin.com/in/tu-moro-netia

Logo Text

Velo Grace

Colors

Designer to choose colors to be used in the design.

```html
<!DOCTYPE html>
<html lang="en">
<head>
<meta charset="utf-8">
<title>Velo Grace – Business Cards</title>
<link rel="stylesheet" href="https://fonts.googleapis.com/css2?family=Questrial&family=Montserrat:wght@400;700&display=swap">
<style>
  :root {
    --bg: #e9eaec;
    --card: #ffffff;
    --card-shade: #e6e7e9;
    --teal: #2fb4bd;
    --teal-deep: #17a3a6;
    --teal-soft: #4fbdc6;
    --ink: #111111;
    --grey: #6d6e71;
    --grey-soft: #7a7b7e;
  }
  * { box-sizing: border-box; margin: 0; padding: 0; }
  html, body { width: 1200px; height: 800px; overflow: hidden; }
  body {
    background: var(--bg);
    position: relative;
    font-family: "Questrial", "Century Gothic", sans-serif;
  }
  .card {
    position: absolute;
    top: 245px;
    width: 540px;
    height: 309px;
    background: var(--card);
    box-shadow: 0 6px 18px rgba(0,0,0,0.12);
    overflow: hidden;
  }
  .card--front {
    left: 40px;
    background: linear-gradient(135deg, var(--card-shade) 0%, #f3f3f4 55%, var(--card) 100%);
  }
  .card--back { left: 620px; }

  .front-sweep {
    position: absolute;
    left: 0; top: 0;
    width: 260px; height: 309px;
  }
  .wordmark {
    position: absolute;
    font-family: "Questrial", "Century Gothic", sans-serif;
    font-weight: 400;
    color: var(--grey);
    white-space: nowrap;
    letter-spacing: 0.5px;
  }
  .wordmark__dot {
    display: inline-block;
    width: 14px; height: 14px;
    border-radius: 50%;
    background: var(--teal);
    margin-right: 12px;
    vertical-align: middle;
    position: relative;
    top: -3px;
  }
  .card--front .wordmark { right: 40px; bottom: 60px; font-size: 38px; }
  .card--back .wordmark { left: 42px; top: 116px; font-size: 38px; }

  .edge-tab {
    position: absolute;
    right: 0; top: 70px;
    width: 22px; height: 62px;
    background: linear-gradient(90deg, var(--teal-soft), var(--teal-deep));
  }
  .contact {
    position: absolute;
    right: 58px;
    top: 82px;
    text-align: right;
  }
  .contact__name {
    font-family: "Montserrat", sans-serif;
    font-weight: 700;
    font-size: 21px;
    letter-spacing: 5px;
    color: var(--ink);
  }
  .contact__role {
    font-family: "Questrial", sans-serif;
    font-size: 12px;
    letter-spacing: 1.5px;
    color: var(--grey);
    margin-top: 2px;
  }
  .contact__lines {
    margin-top: 32px;
    list-style: none;
    font-size: 12.5px;
    color: var(--grey-soft);
    line-height: 26px;
  }
  .contact__lines li { position: relative; }
  .icon {
    position: absolute;
    right: -30px;
    top: 5px;
    width: 16px; height: 16px;
  }
</style>
</head>
<body>

  <section class="card card--front" aria-label="Card front">
    <svg class="front-sweep" viewBox="0 0 260 309" aria-hidden="true">
      <defs>
        <linearGradient id="sweepFill" x1="0" y1="1" x2="1" y2="0">
          <stop offset="0" stop-color="#17a3a6"/>
          <stop offset="1" stop-color="#4fbdc6"/>
        </linearGradient>
      </defs>
      <path d="M0 0 L90 0 Q260 120 240 309 L0 309 Z" fill="url(#sweepFill)"/>
    </svg>
    <div class="wordmark"><span class="wordmark__dot"></span>Velo Grace</div>
  </section>

  <section class="card card--back" aria-label="Card back">
    <div class="wordmark"><span class="wordmark__dot"></span>Velo Grace</div>
    <div class="edge-tab"></div>
    <div class="contact">
      <p class="contact__name">Lucien Marbot</p>
      <p class="contact__role">Sales &amp; Marketing Director</p>
      <ul class="contact__lines">
        <li>(843) 555-0148
          <svg class="icon" viewBox="0 0 16 16" aria-hidden="true">
            <circle cx="8" cy="8" r="8" fill="var(--teal)"/>
            <path d="M5.2 4.2l1.6-.3.8 1.9-1 .8a5 5 0 0 0 2.8 2.8l.8-1 1.9.8-.3 1.6c-3.8.3-7-2.9-6.6-6.6z" fill="#fff"/>
          </svg>
        </li>
        <li>lucienmarbot@velogracestudio.com
          <svg class="icon" viewBox="0 0 16 16" aria-hidden="true">
            <circle cx="8" cy="8" r="8" fill="var(--teal)"/>
            <circle cx="8" cy="8" r="4.6" fill="none" stroke="#fff" stroke-width="1.1"/>
            <path d="M3.4 8h9.2M8 3.4c-2 2.6-2 6.6 0 9.2M8 3.4c2 2.6 2 6.6 0 9.2" fill="none" stroke="#fff" stroke-width="0.9"/>
          </svg>
        </li>
      </ul>
    </div>
  </section>

</body>
</html>
```